Steelcrest Process Systems. Needs a Business Card Design

We need a business card design for an engineering company which supplies industrial components (pumps, compressors, mechanical seals) provides repairs and services for above mentioned equipments. We offer a uniqe engineering solutions which help our customers to increase the productivness of their manufacturings, and energy savings.

Target Market(s)

Chemical and energy plants, refineries. Food industry and private consumers in a less.

Industry/Entity Type

Business

Contact Information for Business Card

Stylish and sleek design oriented on industrial area.

Requirements
Should not have
• company name shortening

```html
<!DOCTYPE html>
<html lang="en">
<head>
<meta charset="utf-8">
<title>Steelcrest Process Systems – Business Card</title>
<link rel="stylesheet" href="https://fonts.googleapis.com/css2?family=Ubuntu:wght@500;700&family=Open+Sans:wght@400;600&display=swap">
<style>
  :root {
    --brand-blue: #1f3c96;
    --ink: #1b1b1b;
    --paper: #ffffff;
    --backdrop: #e9e9ec;
    --accent-red: #ea4335;
  }
  * { box-sizing: border-box; margin: 0; padding: 0; }
  html, body { width: 1200px; height: 1200px; overflow: hidden; }
  body {
    background: var(--backdrop);
    display: flex;
    flex-direction: column;
    align-items: center;
    justify-content: center;
    gap: 60px;
    font-family: "Open Sans", sans-serif;
  }
  .card {
    position: relative;
    width: 900px;
    height: 514px;
    overflow: hidden;
    box-shadow: 0 6px 18px rgba(0,0,0,0.18);
  }

  /* Front */
  .card-front { background: var(--brand-blue); color: var(--paper); }
  .front-brand {
    position: absolute;
    left: 90px;
    top: 170px;
  }
  .front-name {
    font-family: "Ubuntu", sans-serif;
    font-weight: 500;
    font-size: 50px;
    letter-spacing: 0.2px;
  }
  .front-web {
    margin-top: 10px;
    margin-left: 110px;
    font-size: 19px;
  }
  .service-line {
    position: absolute;
    left: 90px;
    bottom: 48px;
    font-size: 19px;
    letter-spacing: 0.3px;
  }
  .service-line .dot { margin: 0 8px; }

  /* Back */
  .card-back { background: var(--paper); color: var(--ink); }
  .back-tab {
    position: absolute;
    left: 0;
    top: 56px;
    width: 22px;
    height: 80px;
    background: var(--brand-blue);
  }
  .holder { position: absolute; left: 66px; top: 62px; }
  .holder-name {
    font-family: "Open Sans", sans-serif;
    font-weight: 600;
    font-size: 30px;
    color: var(--brand-blue);
    text-transform: uppercase;
    letter-spacing: 0.5px;
  }
  .holder-title { font-size: 17px; text-transform: uppercase; margin-top: 2px; }

  .contact-list {
    position: absolute;
    left: 46px;
    top: 276px;
    list-style: none;
    font-size: 19px;
  }
  .contact-list li { display: flex; align-items: center; gap: 12px; height: 30px; }
  .contact-list svg { width: 20px; height: 20px; flex: none; }

  .wordmark {
    position: absolute;
    right: 60px;
    top: 150px;
    display: flex;
    flex-direction: column;
    align-items: flex-end;
    gap: 18px;
  }
  .wordmark-dot {
    width: 70px; height: 70px;
    border-radius: 50%;
    background: var(--accent-red);
    margin-right: 110px;
  }
  .wordmark-name {
    font-family: "Ubuntu", sans-serif;
    font-weight: 500;
    font-size: 36px;
    color: var(--brand-blue);
  }
  .address {
    position: absolute;
    right: 120px;
    bottom: 56px;
    font-size: 18px;
    text-transform: uppercase;
    line-height: 1.45;
    letter-spacing: 0.4px;
  }
</style>
</head>
<body>

  <section class="card card-front" aria-label="Card front">
    <div class="front-brand">
      <div class="front-name">Steelcrest Process Systems</div>
      <div class="front-web">www.steelcrestprocess.com</div>
    </div>
    <p class="service-line">
      Pump Equipment<span class="dot">●</span>Sealing Solutions<span class="dot">●</span>Compressor Components<span class="dot">●</span>Services
    </p>
  </section>

  <section class="card card-back" aria-label="Card back">
    <div class="back-tab"></div>
    <div class="holder">
      <div class="holder-name">Daniel-Martin Reyes</div>
      <div class="holder-title">Vice President</div>
    </div>

    <ul class="contact-list">
      <li>
        <svg viewBox="0 0 20 20"><circle cx="10" cy="10" r="10" fill="#1f3c96"/><path d="M6.5 5.5l2 0 1 2.5-1.2 1a6 6 0 0 0 2.7 2.7l1-1.2 2.5 1v2a1 1 0 0 1-1 1A8 8 0 0 1 5.5 6.5a1 1 0 0 1 1-1z" fill="#fff"/></svg>
        555-014-2730
      </li>
      <li>
        <svg viewBox="0 0 20 20"><circle cx="10" cy="10" r="10" fill="#1f3c96"/><rect x="7" y="4.5" width="6" height="11" rx="1" fill="#fff"/><rect x="8" y="6" width="4" height="7" fill="#1f3c96"/></svg>
        555-014-2791
      </li>
      <li>
        <svg viewBox="0 0 20 20"><circle cx="10" cy="10" r="10" fill="#1f3c96"/><rect x="5" y="6.5" width="10" height="7" fill="#fff"/><path d="M5 6.5l5 4 5-4" stroke="#1f3c96" stroke-width="1.2" fill="none"/></svg>
        info@steelcrestprocess.com
      </li>
      <li>
        <svg viewBox="0 0 20 20"><circle cx="10" cy="10" r="9" fill="none" stroke="#1f3c96" stroke-width="1.6"/><ellipse cx="10" cy="10" rx="4" ry="9" fill="none" stroke="#1f3c96" stroke-width="1.4"/><path d="M1 10h18M2.5 6h15M2.5 14h15" stroke="#1f3c96" stroke-width="1.2"/></svg>
        www.steelcrestprocess.com
      </li>
    </ul>

    <div class="wordmark">
      <div class="wordmark-dot"></div>
      <div class="wordmark-name">Steelcrest Process Systems</div>
    </div>

    <address class="address" style="font-style:normal">
      14 Foundry Park Drive<br>
      Millbrook, PA 17020
    </address>
  </section>

</body>
</html>
```